Logo design and Businesscard and letterhead for Technology Company

We need logo design for a new company based in Atlanta called "Plovenix". We provide information about technology Product and service provider companies, information about their Products and services. Our initial focus is to List various companies and their products, various consulting companies and their services. We want to convey the message that this will be one stop shop to find out all the information to make smart technology decisions

I am looking for Logo, Business Card and Letterhead.

Target Market(s)

Companies that have IT department, IT users such as Developers, Managers, C level, Technology Product companies , Consulting companies and service providers.

Industry/Entity Type

It Company

Requirements
Must have
• Looking for some Unique design idea.
Nice to have
• I want something that connects information across technologies between technology buyers and sellers.
Should not have
• No puzzle design.

```html
<!DOCTYPE html>
<html lang="en">
<head>
<meta charset="utf-8">
<title>Plovenix – Brand Stationery</title>
<link href="https://fonts.googleapis.com/css2?family=Outfit:wght@400;500;600&display=swap" rel="stylesheet">
<style>
  :root{
    --navy:#1b2f86;
    --navy-deep:#14206a;
    --blue:#1e56b0;
    --sky:#2f8fd6;
    --green:#8fbe0c;
    --ink:#1b2f86;
    --paper:#ffffff;
    --rule:#3a3a3a;
    --shadow:rgba(0,0,0,.18);
  }
  *{margin:0;padding:0;box-sizing:border-box}
  html,body{width:1200px;height:805px;overflow:hidden;background:var(--paper)}
  body{position:relative;font-family:"Outfit",sans-serif;color:var(--ink)}
  .abs{position:absolute}
  .mark-dot{position:absolute;border-radius:50%;background:radial-gradient(circle at 35% 35%,var(--sky),var(--navy) 75%)}
  .mark-dot.silver{background:radial-gradient(circle at 35% 35%,#ffffff,#c9ced6 70%)}
  .mark-shadow{position:absolute;border-radius:50%;background:radial-gradient(ellipse at center,var(--shadow),transparent 70%)}
  .wordmark{position:absolute;font-weight:600;color:var(--green);line-height:1;letter-spacing:-.5px;white-space:nowrap}
  .tagline{position:absolute;font-weight:400;color:var(--navy);white-space:nowrap;line-height:1}
  .wave-band{position:absolute;background:
      linear-gradient(160deg,rgba(255,255,255,.08) 0 20%,transparent 20% 35%,rgba(0,0,0,.12) 35% 50%,transparent 50%),
      linear-gradient(90deg,var(--navy-deep),var(--blue) 45%,var(--navy) 100%)}

  /* Letterhead */
  .letterhead{position:absolute;left:27px;top:26px;width:579px;height:750px;border:1px solid var(--rule);background:var(--paper)}
  .letterhead .contact{position:absolute;right:33px;top:27px;text-align:right;font-size:9px;line-height:13.4px;color:var(--navy);font-style:normal}
  .label{color:var(--green)}
  .letterhead .wave-band{left:0;right:0;bottom:0;height:67px}

  /* Banner */
  .banner{left:643px;top:27px;width:522px;height:101px}

  /* Large lockups */
  .lockup .wordmark{left:790px;font-size:76px;letter-spacing:0}
  .lockup .tagline{left:857px;font-size:11.5px;letter-spacing:.3px}

  /* Cards */
  .card-front{position:absolute;left:650px;top:573px;width:241px;height:147px;border:1px solid var(--rule);border-radius:13px;background:var(--paper)}
  .card-back{left:930px;top:573px;width:241px;height:147px;border-radius:13px;overflow:hidden}
  .person{position:absolute;left:22px;top:84px}
  .person-name{font-size:10.5px;font-weight:500;color:var(--navy)}
  .person-role{font-size:8px;color:var(--green);margin-top:1px}
  .card-contact{position:absolute;left:129px;top:68px;font-size:8px;line-height:14.1px;color:var(--navy);font-style:normal}
  .card-contact .row{display:flex}
  .card-contact .row .label{width:19px}
  .web{position:absolute;left:98px;top:66px;font-size:10px;font-weight:600;color:var(--green)}
</style>
</head>
<body>

<!-- Letterhead -->
<section class="letterhead" aria-label="Letterhead">
  <div class="mark-dot" style="left:25px;top:21px;width:48px;height:48px"></div>
  <div class="mark-shadow" style="left:30px;top:74px;width:38px;height:6px"></div>
  <div class="wordmark" style="left:82px;top:26px;font-size:31px">Plovenix</div>
  <div class="tagline" style="left:83px;top:59px;font-size:5.4px">Information about Technology Products &amp; Services</div>
  <address class="contact">
    2180 Larkmere Avenue, Atlanta, GA 30318<br>
    <span class="label">P:</span> (404) 555-0172&nbsp;&nbsp;<span class="label">F:</span> (404) 555 0189<br>
    <span class="label">E:</span> info@plovenix.com&nbsp;&nbsp;&nbsp;<span class="label">W:</span> www.plovenix.com
  </address>
  <div class="wave-band" role="img" aria-label="Blue wave band with faint circuit-board pattern"></div>
</section>

<!-- Banner -->
<section class="abs banner" aria-label="Web banner">
  <div class="wave-band" role="img" aria-label="Blue wave background with faint circuit-board pattern" style="inset:0"></div>
  <div class="mark-dot silver" style="left:31px;top:5px;width:72px;height:72px"></div>
  <div class="wordmark" style="left:118px;top:18px;font-size:50px">Plovenix</div>
  <div class="tagline" style="left:162px;top:76px;font-size:8.5px;color:#ffffff">Information about Technology Products &amp; Services</div>
</section>

<!-- Primary logo lockup -->
<section class="abs lockup" aria-label="Primary logo" style="left:0;top:0">
  <div class="mark-dot" style="left:669px;top:198px;width:103px;height:103px"></div>
  <div class="mark-shadow" style="left:675px;top:316px;width:90px;height:12px"></div>
  <div class="wordmark" style="top:200px">Plovenix</div>
  <div class="tagline" style="top:277px">Information about Technology Products &amp; Services</div>
</section>

<!-- Alternate logo lockup -->
<section class="abs lockup" aria-label="Alternate logo" style="left:0;top:0">
  <div class="mark-dot silver" style="left:669px;top:396px;width:103px;height:103px"></div>
  <div class="mark-shadow" style="left:670px;top:513px;width:100px;height:14px"></div>
  <div class="wordmark" style="top:398px">Plovenix</div>
  <div class="tagline" style="top:475px">Information about Technology Products &amp; Services</div>
</section>

<!-- Business card front -->
<section class="card-front" aria-label="Business card front">
  <div class="mark-dot" style="left:69px;top:18px;width:34px;height:34px"></div>
  <div class="mark-shadow" style="left:72px;top:56px;width:28px;height:5px"></div>
  <div class="wordmark" style="left:108px;top:23px;font-size:21px">Plovenix</div>
  <div class="tagline" style="left:129px;top:46px;font-size:3.6px">Information about Technology Products &amp; Services</div>
  <div class="person">
    <div class="person-name">Dana REYES</div>
    <div class="person-role">Director</div>
  </div>
  <address class="card-contact">
    <div>2180 Larkmere Avenue,</div>
    <div>Atlanta, GA 30318</div>
    <div class="row"><span class="label">P:</span><span>(404) 555-0172</span></div>
    <div class="row"><span class="label">F:</span><span>(404) 555 0189</span></div>
    <div class="row"><span class="label">E:</span><span>info@plovenix.com</span></div>
  </address>
</section>

<!-- Business card back -->
<section class="abs card-back" aria-label="Business card back">
  <div class="wave-band" role="img" aria-label="Blue wave background with faint circuit-board pattern" style="inset:0"></div>
  <div class="mark-dot silver" style="left:23px;top:35px;width:66px;height:66px"></div>
  <div class="web">www.plovenix.com</div>
</section>

</body>
</html>
```